Wedding Postcard Design

We want to design a postcard using our photo's from our wedding and send the postcards as 'Thank You's' to the guests from our wedding. On the front we would like to use the 3 x photos we have uploaded and perhaps with white boarders and on the back just lines for the addresses.
Ideally we would like them slightly larger size than the standard postcard if possible.
Updates

Sorry for the change however we feel 5 photos is too many and too crowded as I am sure you would agree.  

Can we possibly reduce it to 3 photos using the following 3:

- black and white photo
- photo with the beach behind us
- close up photo on the wharf where he is standing behind me and there is a little yellow boat behind us

 

                                                                 

Target Market(s)

Our friends

Industry/Entity Type

Wedding

```html
<!DOCTYPE html>
<html lang="en">
<head>
<meta charset="utf-8">
<title>Wedding Thank You Postcard</title>
<link rel="stylesheet" href="https://fonts.googleapis.com/css2?family=Pinyon+Script&family=Petit+Formal+Script&family=Tangerine:wght@700&family=Arimo:wght@400&display=swap">
<style>
  :root {
    --backdrop: #e7e4df;
    --card: #ffffff;
    --silver-light: #f2f2f2;
    --silver-mid: #d3d3d3;
    --silver-dark: #b9b9b9;
    --accent-blue: #1aa3e6;
    --ink: #4a4a4a;
    --rule-violet: #8a7fd0;
    --photo-mono-a: #8c8c8c;
    --photo-mono-b: #3a3a3a;
    --photo-beach-a: #9cc3e4;
    --photo-beach-b: #6f9a5a;
    --photo-wharf-a: #c7d8e6;
    --photo-wharf-b: #6a7a5a;
  }
  * { margin: 0; padding: 0; box-sizing: border-box; }
  html, body { width: 1200px; height: 438px; overflow: hidden; }
  body { background: var(--backdrop); position: relative; }

  .postcard {
    position: absolute;
    top: 32px;
    width: 564px;
    height: 374px;
    background: var(--card);
    overflow: hidden;
  }
  .postcard--front { left: 26px; }
  .postcard--back { left: 612px; }

  .photo { position: absolute; }
  .photo--mono {
    left: 0; top: 20px; width: 320px; height: 330px;
    background: linear-gradient(160deg, var(--photo-mono-b) 0%, var(--photo-mono-a) 55%, var(--photo-mono-b) 100%);
  }
  .photo--beach {
    left: 326px; top: 50px; width: 238px; height: 140px;
    background: linear-gradient(180deg, var(--photo-beach-a) 0%, #d9e7f1 55%, var(--photo-beach-b) 100%);
  }
  .photo--wharf {
    left: 326px; top: 198px; width: 238px; height: 150px;
    background: linear-gradient(180deg, var(--photo-wharf-a) 0%, #aab9c6 55%, var(--photo-wharf-b) 100%);
  }

  .swoosh { position: absolute; left: 0; top: 0; width: 564px; height: 374px; }

  .front-greeting {
    position: absolute;
    left: 54px; top: 332px;
    font-family: "Pinyon Script", cursive;
    font-size: 30px;
    color: var(--ink);
  }

  .back-message { position: absolute; left: 20px; top: 78px; color: var(--ink); }
  .back-message__title {
    font-family: "Pinyon Script", cursive;
    font-size: 48px; font-weight: 400; line-height: 1; white-space: nowrap;
  }
  .back-message__subtitle {
    font-family: "Tangerine", cursive;
    font-size: 46px; font-weight: 700; line-height: 1; margin-top: 6px; padding-left: 6px; white-space: nowrap;
  }
  .back-message__body {
    font-family: "Petit Formal Script", cursive;
    font-size: 11.3px; line-height: 19.5px; margin-top: 6px; padding-left: 6px; white-space: nowrap;
  }

  .divider {
    position: absolute; left: 281px; top: 62px; width: 1px; height: 248px;
    background: var(--rule-violet);
  }
  .postage-indicia {
    position: absolute; left: 492px; top: 86px; width: 48px; height: 48px;
    border: 1px solid #333; background: var(--card);
    font-family: "Arimo", sans-serif; font-size: 6px; line-height: 7.5px;
    text-align: center; color: #222; padding-top: 3px; white-space: nowrap;
  }
  .postage-indicia__paid { font-size: 8px; line-height: 9px; }
  .address-lines { position: absolute; left: 326px; top: 158px; width: 213px; }
  .address-lines__line { height: 1px; background: var(--rule-violet); margin-bottom: 26.5px; }
</style>
</head>
<body>

<section class="postcard postcard--front" aria-label="Postcard front">
  <div class="photo photo--mono" role="img" aria-label="Black and white photo of the bride and groom walking on a forest path"></div>
  <div class="photo photo--beach" role="img" aria-label="Photo of the couple standing on grass with the beach behind them"></div>
  <div class="photo photo--wharf" role="img" aria-label="Close-up photo of the couple on the wharf, groom standing behind the bride"></div>

  <svg class="swoosh" viewBox="0 0 564 374" aria-hidden="true">
    <defs>
      <linearGradient id="silverFront" x1="0" y1="0" x2="1" y2="0">
        <stop offset="0" stop-color="var(--silver-dark)"/>
        <stop offset="0.35" stop-color="var(--silver-light)"/>
        <stop offset="0.65" stop-color="var(--silver-mid)"/>
        <stop offset="1" stop-color="var(--silver-light)"/>
      </linearGradient>
    </defs>
    <path d="M0,0 H564 V54 C470,74 380,72 290,54 C190,34 90,28 0,40 Z" fill="url(#silverFront)"/>
    <path d="M0,44 C80,30 180,28 270,44 C180,36 80,42 0,60 Z" fill="var(--accent-blue)"/>
    <path d="M410,66 C470,68 520,60 564,48 V62 C520,72 460,74 410,66 Z" fill="var(--accent-blue)"/>
    <path d="M0,338 C110,316 240,320 330,342 C420,364 500,358 564,344 V374 H0 Z" fill="url(#silverFront)"/>
    <path d="M0,344 C70,328 150,322 230,330 C150,330 70,340 0,360 Z" fill="var(--accent-blue)"/>
    <path d="M330,338 C420,360 500,354 564,336 V348 C500,364 420,366 330,338 Z" fill="var(--accent-blue)"/>
  </svg>

  <p class="front-greeting">Thank you</p>
</section>

<section class="postcard postcard--back" aria-label="Postcard back">
  <svg class="swoosh" viewBox="0 0 564 374" aria-hidden="true">
    <defs>
      <linearGradient id="silverBack" x1="0" y1="0" x2="1" y2="0">
        <stop offset="0" stop-color="var(--silver-dark)"/>
        <stop offset="0.4" stop-color="var(--silver-light)"/>
        <stop offset="0.7" stop-color="var(--silver-mid)"/>
        <stop offset="1" stop-color="var(--silver-light)"/>
      </linearGradient>
    </defs>
    <path d="M0,0 H564 V48 C470,58 400,56 320,40 C220,22 100,18 0,24 Z" fill="url(#silverBack)"/>
    <path d="M0,30 C90,20 200,22 260,30 C180,28 90,34 0,44 Z" fill="var(--accent-blue)"/>
    <path d="M390,46 C460,54 520,52 564,46 V54 C510,60 450,58 390,46 Z" fill="var(--accent-blue)"/>
    <path d="M0,322 C110,306 240,312 330,330 C420,348 500,342 564,330 V374 H0 Z" fill="url(#silverBack)"/>
    <path d="M0,330 C70,318 150,314 230,318 C150,320 70,328 0,344 Z" fill="var(--accent-blue)"/>
    <path d="M300,326 C400,348 490,344 564,322 V334 C490,354 400,352 300,326 Z" fill="var(--accent-blue)"/>
  </svg>

  <div class="back-message">
    <h1 class="back-message__title">Thank you</h1>
    <p class="back-message__subtitle">for attending</p>
    <p class="back-message__body">Lorem ipsum dolor sit amet, consect-<br>etuer adipiscing elit, sed diam non-<br>ummy nibh euismod tincidunt ut<br>laoreet dolore magna aliquam erat<br>volutpat.</p>
  </div>

  <div class="divider"></div>

  <div class="postage-indicia">
    PRSRT STD<br>ECRWSS<br>POSTAGE<br><span class="postage-indicia__paid">PAID</span><br>Route Mail
  </div>

  <div class="address-lines">
    <div class="address-lines__line"></div>
    <div class="address-lines__line"></div>
    <div class="address-lines__line"></div>
    <div class="address-lines__line"></div>
  </div>
</section>

</body>
</html>
```